Southport Billboard for Hiring more CDL drivers

I need a catch design for a bill board (size 10ft by 36 ft) to catch the attention for semi truck drivers.
In the design I want it to include:
-My company logo along with my website(brisklanefreighters.com) and my number(503-217-6095) for contact info.
-I also need it to say earn up to $90,000 a year
-I will send a few photos to choose from
-I need the logo to look clean and simple! I don't want it to be cluttered just clean, simple and catchy.!

Target Market(s)

CDL Class A holders
Semi Truck Drivers

Industry/Entity Type

Trucking Company

Font styles to use
Other font styles liked:
• a font to match my logo

Requirements
Must have
• "Make up to $90,000"
"brisklanefreighters.com"
"503-217-6095"

```html
<!DOCTYPE html>
<html lang="en">
<head>
<meta charset="utf-8">
<title>Brisk Lane Freighters — Driver Hiring Billboard</title>
<link rel="stylesheet" href="https://fonts.googleapis.com/css2?family=Oswald:wght@700&family=Arimo:wght@700&display=swap">
<style>
  :root {
    --canvas: #ffffff;
    --board-dark: #222522;
    --brand-red: #e31b23;
    --text-white: #ffffff;
    --slant-grey: #8e9092;
    --photo-sky: #c9d3dc;
    --photo-ground: #6f7479;
  }
  * { margin: 0; padding: 0; box-sizing: border-box; }
  html, body {
    width: 1200px;
    height: 1200px;
    overflow: hidden;
    background: var(--canvas);
  }
  .billboard {
    position: absolute;
    left: 75px;
    top: 454px;
    width: 1050px;
    height: 292px;
    background: var(--board-dark);
    overflow: hidden;
  }
  .billboard__shapes {
    position: absolute;
    inset: 0;
  }
  .brand-name {
    position: absolute;
    left: 30px;
    top: 58px;
    width: 270px;
    font-family: "Oswald", sans-serif;
    font-weight: 700;
    font-size: 54px;
    line-height: 1.08;
    color: var(--text-white);
    text-transform: uppercase;
  }
  .headline {
    position: absolute;
    left: 326px;
    top: 28px;
    width: 360px;
    text-align: center;
    font-family: "Oswald", sans-serif;
    font-weight: 700;
    text-transform: uppercase;
    color: var(--text-white);
  }
  .headline__lead,
  .headline__tail {
    display: block;
    font-size: 36px;
    line-height: 1.05;
  }
  .headline__amount {
    display: block;
    font-size: 90px;
    line-height: 1.02;
    color: var(--brand-red);
    letter-spacing: -1px;
  }
  .contact {
    position: absolute;
    top: 234px;
    height: 47px;
    display: flex;
    align-items: center;
    gap: 10px;
    font-family: "Arimo", sans-serif;
    font-weight: 700;
    color: var(--text-white);
    white-space: nowrap;
  }
  .contact--phone { left: 28px; font-size: 42px; }
  .contact--web { left: 486px; font-size: 36px; }
  .contact__icon { width: 38px; height: 38px; flex: none; }
  .truck-photo {
    position: absolute;
    left: 700px;
    top: 0;
    width: 350px;
    height: 234px;
  }
</style>
</head>
<body>
  <main class="billboard" aria-label="Driver hiring billboard">
    <svg class="billboard__shapes" viewBox="0 0 1050 292" width="1050" height="292" aria-hidden="true">
      <defs>
        <linearGradient id="truckPhotoTone" x1="0" y1="0" x2="0" y2="1">
          <stop offset="0" stop-color="var(--photo-sky)"/>
          <stop offset="0.55" stop-color="#9aa6b0"/>
          <stop offset="1" stop-color="var(--photo-ground)"/>
        </linearGradient>
      </defs>
      <polygon points="738,0 753,0 640,292 625,292" fill="var(--slant-grey)"/>
      <polygon points="753,0 1050,0 1050,292 640,292" fill="url(#truckPhotoTone)"/>
      <rect x="0" y="234" width="1050" height="47" fill="var(--brand-red)"/>
    </svg>
    <div class="truck-photo" role="img" aria-label="Photo of two semi trucks, one red and one blue, parked side by side"></div>

    <h1 class="brand-name">Brisk Lane Freighters</h1>

    <p class="headline">
      <span class="headline__lead">Earn up to</span>
      <span class="headline__amount">$90,000</span>
      <span class="headline__tail">a year</span>
    </p>

    <p class="contact contact--phone">
      <svg class="contact__icon" viewBox="0 0 40 40" aria-hidden="true">
        <circle cx="20" cy="20" r="17" fill="none" stroke="var(--board-dark)" stroke-width="3"/>
        <path d="M14 11 l4 0 l1.5 5 l-2.5 2 q2 5 6 7 l2 -2.5 l5 1.5 l0 4 q-1 2 -4 2 q-13 -3 -14 -15 q0 -3 2 -4z" fill="var(--board-dark)"/>
      </svg>
      <span>503-217-6095</span>
    </p>

    <p class="contact contact--web">
      <svg class="contact__icon" viewBox="0 0 40 40" aria-hidden="true">
        <circle cx="20" cy="20" r="17" fill="none" stroke="var(--board-dark)" stroke-width="3"/>
        <g fill="none" stroke="var(--board-dark)" stroke-width="1.8">
          <circle cx="20" cy="20" r="10"/>
          <ellipse cx="20" cy="20" rx="4.5" ry="10"/>
          <line x1="10" y1="20" x2="30" y2="20"/>
          <line x1="12" y1="14.5" x2="28" y2="14.5"/>
          <line x1="12" y1="25.5" x2="28" y2="25.5"/>
        </g>
      </svg>
      <span>brisklanefreighters.com</span>
    </p>
  </main>
</body>
</html>
```